update of B2B website and conversion to single page

The current website needs to be modernized. I want what is commonly called a single page website. It is not actually a single page. See some examples here:
https://www.brivolane.example/
https://www.quenzo.example/
https://www.tarnwickhub.example/
Most or all graphics will be replaced.
Please see the attached spreadsheet for a rough draft of the home page layout. Convert the existing website at https://www.zorbilinfo.example/ to a single page website. We will provide the page content. You will provide all of the design, graphics, development, production deployment. etc. The look and feel should be corporate, polished, premium.

```html
<!DOCTYPE html>
<html lang="en">
<head>
<meta charset="utf-8">
<title>Zorbil Data – Enterprise Data Quality</title>
<link rel="stylesheet" href="https://fonts.googleapis.com/css2?family=Oswald:wght@400;500&family=Roboto:wght@300;400;500&display=swap">
<style>
:root{
  --navy:#0f1f66;
  --navy-deep:#0c1a5c;
  --yellow:#fcc20f;
  --blue-text:#2d3f8f;
  --ink:#1e2233;
  --muted:#8a90a4;
  --pale:#f3f4f7;
  --line:#d7dae3;
  --white:#ffffff;
}
*{box-sizing:border-box;margin:0;padding:0}
html,body{width:1200px;height:3564px;overflow:hidden}
body{position:relative;background:var(--white);font-family:'Roboto',sans-serif;color:var(--ink)}
.abs{position:absolute}
.heading{font-family:'Oswald',sans-serif;font-weight:400}

/* header */
.brand{left:40px;top:22px;display:flex;align-items:center;gap:10px}
.brand-dot{width:40px;height:40px;border-radius:50%;background:var(--navy)}
.brand-name{font-family:'Roboto',sans-serif;font-weight:500;font-size:30px;color:var(--navy)}
.brand-tag{left:92px;top:60px;font-size:12px;color:var(--navy);font-weight:500}
.nav{left:412px;top:42px;width:396px;display:flex;justify-content:space-between;font-size:12px;color:var(--navy);white-space:nowrap}
.nav a{color:inherit;text-decoration:none}
.nav .current{text-decoration:underline}
.call{left:846px;top:30px;font-size:16px;line-height:20px;color:var(--navy);font-family:'Oswald',sans-serif;white-space:nowrap}
.call small{display:block;font-family:'Roboto',sans-serif;font-size:11px;line-height:14px;color:var(--blue-text)}
.btn{display:flex;align-items:center;justify-content:center;font-family:'Oswald',sans-serif;font-size:13px;text-transform:uppercase;letter-spacing:.3px}
.btn-yellow{background:var(--yellow);color:var(--ink)}
.btn-outline{border:2px solid var(--yellow);color:var(--navy);background:transparent}
.btn-navy-out{border:2px solid var(--yellow);color:var(--white)}

/* hero */
.hero-art{left:60px;top:120px;width:650px;height:510px;border-radius:20px;background:radial-gradient(ellipse at 50% 55%,#dfe4fb 0%,#eef1fd 55%,#ffffff 85%)}
.hero-title{left:780px;top:214px;font-size:40px;line-height:48px;font-weight:300;color:var(--blue-text)}

/* band */
.band{left:0;top:640px;width:1200px;height:440px;background:var(--navy)}
.band-title{left:0;top:755px;width:1200px;text-align:center;font-size:26px;color:var(--white)}
.feat{width:240px;text-align:center;color:var(--white);font-size:15px;line-height:20px}
.feat svg{display:block;margin:0 auto 26px}

/* tabs */
.tab{top:1133px;font-size:14px;font-family:'Oswald',sans-serif;text-transform:uppercase;width:240px;text-align:center}
.tab-line{top:1167px;height:2px;width:240px}

/* feature list */
.fl{left:38px;width:562px;height:133px;padding:30px 40px 0 83px;position:absolute;border-bottom:1px solid var(--line)}
.fl h3{font-size:20px;font-weight:400;margin-bottom:10px}
.fl p{font-size:12px;line-height:17px;color:var(--muted)}
.fl.active{background:var(--navy);color:var(--white);border:none}
.fl.active p{color:#c7cce6}
.fl-box{position:absolute;left:20px;top:22px;width:54px;height:40px;border:1px solid #c9cdd8;opacity:.6}
.fl.active .fl-box{border-color:#5d6aa6}
.fl-arrow{left:598px;top:1250px}
.feature-photo{left:600px;top:1200px;width:560px;height:400px;background:linear-gradient(120deg,#dcd4cb 0%,#b9a898 45%,#5c4638 75%,#2d2a33 100%)}

/* connectors */
.conn-title{left:0;top:1718px;width:1200px;text-align:center;font-size:29px;color:var(--blue-text)}
.conn-sub{left:0;top:1760px;width:1200px;text-align:center;font-size:19px;color:var(--muted)}
.conn-sub b{font-weight:400;color:var(--blue-text)}
.conn-rule{left:566px;top:1810px;width:68px;height:1px;background:var(--line)}
.db-title{left:0;top:1838px;width:1200px;text-align:center;font-size:19px;color:#a7aecd}
.db-sub{left:0;top:1868px;width:1200px;text-align:center;font-size:12px;color:#b4b8c6}

/* why */
.why{left:0;top:2096px;width:1200px;height:425px;background:var(--yellow)}
.why-title{left:0;top:2200px;width:1200px;text-align:center;font-size:28px;color:var(--blue-text)}
.why-item{width:240px;text-align:center;top:2286px}
.why-item svg{display:block;margin:0 auto 22px}
.why-item h4{font-family:'Oswald',sans-serif;font-weight:500;font-size:14px;color:var(--navy);text-transform:uppercase}
.why-item p{font-size:13px;color:var(--ink);margin-top:4px}

/* updates */
.upd-title{left:0;top:2632px;width:1200px;text-align:center;font-size:28px;color:var(--blue-text)}
.post{top:2706px;width:242px}
.post-img{height:160px;width:100%}
.post-meta{margin-top:28px;font-size:10px;color:var(--muted);text-transform:uppercase}
.post h5{margin-top:12px;font-size:15px;font-weight:400;line-height:19px;color:var(--ink)}
.post h5.linked{color:var(--blue-text);text-decoration:underline}

/* footer */
.footer{left:0;top:3065px;width:1200px;height:499px;background:var(--navy)}
.f-head{font-family:'Oswald',sans-serif;font-size:14px;color:var(--white);text-transform:uppercase;top:3180px}
.f-phone{left:200px;top:3222px;font-family:'Oswald',sans-serif;font-size:30px;color:var(--white);letter-spacing:1px}
.f-mail{left:200px;top:3265px;font-size:12px;color:#c7cce6}
.f-addr{left:200px;top:3300px;font-size:12px;line-height:17px;color:#c7cce6}
.field{background:#b9bfd8;height:30px;font-size:12px;color:#6b7190;padding:8px 10px}
.social{left:1078px;width:22px;height:22px;border-radius:50%;background:#b9bfd8}
.f-note{left:0;width:1200px;text-align:center;font-size:11px;color:#c7cce6}
</style>
</head>
<body>

<!-- header -->
<div class="abs brand"><span class="brand-dot"></span><span class="brand-name">Zorbil Data</span></div>
<div class="abs brand-tag">Enterprise Data Quality Made Easy</div>
<nav class="abs nav">
  <a class="current">Connectors</a><a>QFeatures</a><a>Why QC*Prime?</a><a>Offers</a><a>Services</a>
</nav>
<div class="abs call">Call Us: 555 - 013 - 0147<small>info@zorbilinfo.example</small></div>
<div class="abs btn btn-yellow" style="left:1040px;top:33px;width:120px;height:32px">Contact us</div>

<!-- hero -->
<div class="abs hero-art" role="img" aria-label="Isometric illustration of people working around a large laptop with data cards, charts and a cloud"></div>
<h1 class="abs hero-title">Enterprise Data<br>Quality and Master<br>Data Management<br>Made Easy</h1>
<div class="abs btn btn-outline" style="left:780px;top:440px;width:202px;height:38px">Start your free trial</div>

<!-- speed band -->
<section class="abs band"></section>
<h2 class="abs band-title heading">Faster, More Powerful, Easy to Use</h2>
<div class="abs feat" style="left:196px;top:838px">
  <svg width="66" height="66" viewBox="0 0 66 66" fill="none" stroke="#fff" stroke-width="2"><rect x="3" y="3" width="60" height="60" rx="4"/><line x1="3" y1="13" x2="63" y2="13"/><circle cx="33" cy="38" r="17"/><ellipse cx="33" cy="38" rx="7" ry="17"/><line x1="16" y1="38" x2="50" y2="38"/></svg>
  Cleanse addresses in 5<br>minutes
</div>
<div class="abs feat" style="left:486px;top:838px">
  <svg width="66" height="66" viewBox="0 0 66 66" fill="none" stroke="#fff" stroke-width="2"><path d="M16 28a10 10 0 0 1 4-19 14 14 0 0 1 26 4 8 8 0 0 1 4 15z"/><rect x="14" y="34" width="14" height="20"/><rect x="38" y="34" width="14" height="20"/><line x1="21" y1="28" x2="21" y2="34"/><line x1="45" y1="28" x2="45" y2="34"/><line x1="8" y1="60" x2="58" y2="60"/></svg>
  Match and merge records in 10<br>minutes
</div>
<div class="abs feat" style="left:760px;top:838px">
  <svg width="66" height="66" viewBox="0 0 66 66" fill="none" stroke="#fff" stroke-width="2"><circle cx="26" cy="28" r="20"/><ellipse cx="26" cy="28" rx="8" ry="20"/><line x1="6" y1="28" x2="46" y2="28"/><rect x="36" y="34" width="24" height="8"/><rect x="36" y="44" width="24" height="8"/><rect x="36" y="54" width="24" height="8"/></svg>
  Master records in 60<br>minutes
</div>

<!-- tabs -->
<div class="abs tab" style="left:343px;color:var(--navy)">Enterprise Data Quality</div>
<div class="abs tab" style="left:640px;color:#b4b8c6">Master Data Management</div>
<div class="abs heading" style="left:594px;top:1131px;color:#b4b8c6;font-size:14px">X</div>
<div class="abs tab-line" style="left:320px;background:var(--navy)"></div>
<div class="abs tab-line" style="left:640px;background:var(--line)"></div>

<!-- feature list -->
<div class="fl active" style="top:1200px"><span class="fl-box"></span><h3>Global address verification</h3><p>QC*Prime data quality software provides a single solution for all of your domestic and international address validation needs. (+)</p></div>
<div class="fl" style="top:1333px;background:var(--pale)"><span class="fl-box"></span><h3>Data cleansing / enrichment</h3><p>QC*Prime fills in the blanks with Name, Address, Phone, Email, Geographic Coordinates, Gender... (+)</p></div>
<div class="fl" style="top:1466px;height:134px;background:var(--pale)"><span class="fl-box"></span><h3>Match and merge</h3><p>QC*Prime accurately matches duplicate records and intelligently merges them into a single best record. (+)</p></div>
<svg class="abs fl-arrow" width="18" height="30" viewBox="0 0 18 30"><path d="M0 0 18 15 0 30z" fill="#0f1f66"/></svg>
<div class="abs feature-photo" role="img" aria-label="Photo of a person in a striped shirt holding a smartphone"></div>

<!-- connectors -->
<h2 class="abs conn-title heading">Application Aware Connectors</h2>
<p class="abs conn-sub">For <b>Veltrix Business Suite</b>, <b>Tarnwick Hub</b> and <b>Corvane</b></p>
<div class="abs conn-rule"></div>
<h3 class="abs db-title heading">Database Aware Connectors</h3>
<p class="abs db-sub">For Norda DB, Plexor SQL Server and Veltrix</p>
<div class="abs btn btn-outline" style="left:520px;top:1934px;width:160px;height:33px">Explore more</div>

<!-- why -->
<section class="abs why"></section>
<h2 class="abs why-title heading">Why Zorbil Data</h2>
<div class="abs why-item" style="left:200px">
  <svg width="66" height="66" viewBox="0 0 66 66" fill="none" stroke="#fff" stroke-width="2.4"><rect x="6" y="10" width="54" height="50" rx="4"/><line x1="6" y1="22" x2="60" y2="22"/><line x1="18" y1="4" x2="18" y2="14"/><line x1="48" y1="4" x2="48" y2="14"/><path d="M20 32h6M30 32h6M40 32h6M20 42h6M30 42h6M40 42h6M20 51h6"/></svg>
  <h4>Batch</h4><p>On your schedule</p>
</div>
<div class="abs why-item" style="left:480px">
  <svg width="66" height="66" viewBox="0 0 66 66" fill="none" stroke="#fff" stroke-width="2.4"><rect x="8" y="4" width="50" height="58" rx="3"/><circle cx="33" cy="30" r="12"/><line x1="42" y1="39" x2="52" y2="50"/><line x1="16" y1="54" x2="32" y2="54"/></svg>
  <h4>Real time/interactive</h4><p>Autocomplete anything, Smart search</p>
</div>
<div class="abs why-item" style="left:760px">
  <svg width="66" height="66" viewBox="0 0 66 66" fill="none" stroke="#fff" stroke-width="2.4"><path d="M33 6a27 27 0 1 0 27 27"/><path d="M33 16a17 17 0 1 0 17 17"/><rect x="34" y="30" width="26" height="20" rx="2"/><path d="M34 34l13 8 13-8"/></svg>
  <h4>Streaming</h4><p>Always in sync</p>
</div>

<!-- updates -->
<h2 class="abs upd-title heading">Latest Update from Zorbil Data</h2>
<article class="abs post" style="left:200px">
  <div class="post-img" role="img" aria-label="Photo of a red broom sweeping papers on a floor" style="background:linear-gradient(160deg,#e7e4e0,#b8aea6 60%,#8e2b2b)"></div>
  <div class="post-meta">Aug 18, 2015 / By Dana Holt</div>
  <h5>Tarnwick Hub usability (part 3 of 3):<br>Deduping</h5>
</article>
<article class="abs post" style="left:480px">
  <div class="post-img" role="img" aria-label="Photo of a hand touching a glowing search bar" style="background:linear-gradient(160deg,#7d8da8,#b9c6da 50%,#4e5d78)"></div>
  <div class="post-meta">Aug 18, 2015 / By Dana Holt</div>
  <h5 class="linked">Tarnwick Hub usability (part 2 of 3):<br>Smart search</h5>
</article>
<article class="abs post" style="left:760px">
  <div class="post-img" role="img" aria-label="Photo of hands typing on a laptop keyboard" style="background:linear-gradient(160deg,#d9d4d2,#a89691 55%,#5c4a55)"></div>
  <div class="post-meta">Aug 18, 2015 / By Dana Holt</div>
  <h5>Tarnwick Hub usability (part 1 of 3):<br>Minimizing data entry</h5>
</article>

<!-- footer -->
<footer class="abs footer"></footer>
<div class="abs f-head" style="left:200px">Need help? Contact us</div>
<div class="abs f-phone">P. 555 . 013 . 0147</div>
<div class="abs f-mail">e. info@zorbilinfo.example</div>
<div class="abs f-addr">Zorbil Data<br>418 Larkfield Way Suite 12<br>Brinmoor, CA 90017</div>
<div class="abs btn btn-yellow" style="left:200px;top:3390px;width:118px;height:32px">Contact us</div>

<div class="abs f-head" style="left:480px">Send us message</div>
<div class="abs field" style="left:480px;top:3231px;width:176px">Enter your Name</div>
<div class="abs field" style="left:672px;top:3231px;width:176px">Email</div>
<div class="abs field" style="left:865px;top:3231px;width:133px">Phone</div>
<div class="abs field" style="left:480px;top:3279px;width:518px;height:93px">Message</div>
<div class="abs btn btn-navy-out" style="left:480px;top:3390px;width:118px;height:32px">Submit</div>

<div class="abs social" style="top:3186px"></div>
<div class="abs social" style="top:3221px"></div>
<div class="abs social" style="top:3257px;background:var(--yellow)"></div>
<div class="abs social" style="top:3294px"></div>
<div class="abs social" style="top:3330px"></div>

<p class="abs f-note" style="top:3474px">QC*Prime is easy-to-use, enterprise data quality software.</p>
<p class="abs f-note" style="top:3495px">© 2018 Zorbil Data</p>

</body>
</html>
```